Business Card Design Project

We need a double-sided business card design for our e-commerce company. Be as creative as you can.

Reason: Change of logo

Target Market(s)

Business owners

Industry/Entity Type

E-Commerce

Requirements
Must have
• Name (editable)
Mobile number -editable
www.velbiro.com - MUST STAND OUT ALONE
Office address:
27 Marlow Street
#09-04 Westbrook Tower
Singapore 048216

```html
<!DOCTYPE html>
<html lang="en">
<head>
<meta charset="utf-8">
<title>Velbiro Business Card</title>
<link rel="stylesheet" href="https://fonts.googleapis.com/css2?family=Open+Sans:wght@700&family=Tinos&display=swap">
<style>
  :root {
    --backdrop: #6b4a33;
    --card-black: #050507;
    --card-edge: #2a2a30;
    --glow-blue: #0d1f5c;
    --orange: #f0782a;
    --web-orange: #e5662a;
    --blue: #3d82d6;
    --text-orange: #f2a23a;
  }
  html, body {
    margin: 0;
    width: 1200px;
    height: 1200px;
    overflow: hidden;
    background: var(--backdrop);
  }
  .canvas {
    position: relative;
    width: 1200px;
    height: 1200px;
  }
  .card {
    position: absolute;
    width: 825px;
    height: 470px;
    border-radius: 70px;
    background: var(--card-black);
    border: 2px solid var(--card-edge);
    box-shadow:
      0 6px 0 -1px #141418,
      0 12px 0 -2px #1c1c22,
      0 18px 0 -3px #111115,
      0 30px 40px rgba(0,0,0,.55);
    overflow: hidden;
    font-family: "Open Sans", Arial, sans-serif;
  }
  .card--front { left: 35px; top: 50px; }
  .card--back  { left: 295px; top: 625px; }
  .card__texture {
    position: absolute;
    inset: 0;
    background: radial-gradient(ellipse 55% 60% at 50% 52%, var(--glow-blue) 0%, #081236 40%, var(--card-black) 85%);
  }
  .card--back .card__texture {
    background: radial-gradient(ellipse 60% 70% at 45% 55%, var(--glow-blue) 0%, #081236 45%, var(--card-black) 88%);
  }
  .brand-name {
    position: absolute;
    margin: 0;
    font-weight: 700;
    color: var(--orange);
    letter-spacing: 1px;
    line-height: 1;
  }
  .card--front .brand-name {
    left: 0; right: 0;
    top: 195px;
    text-align: center;
    font-size: 104px;
  }
  .card--back .brand-name {
    left: 385px;
    top: 40px;
    font-size: 62px;
  }
  .website {
    position: absolute;
    font-family: "Tinos", "Times New Roman", serif;
    color: var(--web-orange);
    letter-spacing: .5px;
    margin: 0;
  }
  .card--front .website {
    left: 0; right: 0;
    top: 410px;
    text-align: center;
    font-size: 25px;
  }
  .card--back .website {
    left: 580px;
    top: 344px;
    font-size: 20px;
  }
  .person {
    position: absolute;
    left: 85px;
    top: 115px;
  }
  .person__name {
    margin: 0;
    font-size: 31px;
    color: var(--orange);
    letter-spacing: 1px;
    line-height: 1.1;
  }
  .person__title {
    margin: 4px 0 0 14px;
    font-size: 15px;
    color: var(--blue);
  }
  .contact {
    position: absolute;
    left: 90px;
    top: 225px;
    margin: 0;
    padding: 0;
    list-style: none;
    font-size: 16px;
    color: var(--text-orange);
  }
  .contact__item {
    display: flex;
    align-items: flex-start;
    gap: 6px;
    line-height: 24px;
  }
  .contact__item--address { margin-top: 38px; }
  .contact__icon { flex: none; margin-top: 5px; }
</style>
</head>
<body>
<main class="canvas">

  <section class="card card--front" aria-label="Card front">
    <div class="card__texture" role="img" aria-label="Dark navy dotted texture glowing blue at the centre"></div>
    <h1 class="brand-name">velbiro</h1>
    <p class="website">WWW.VELBIRO.COM</p>
  </section>

  <section class="card card--back" aria-label="Card back">
    <div class="card__texture" role="img" aria-label="Dark navy dotted texture glowing blue at the centre"></div>
    <p class="brand-name">velbiro</p>

    <div class="person">
      <h2 class="person__name">MARCUS LEE</h2>
      <p class="person__title">FOUNDER/OWNER</p>
    </div>

    <ul class="contact">
      <li class="contact__item">
        <svg class="contact__icon" width="14" height="14" viewBox="0 0 14 14" aria-hidden="true">
          <circle cx="7" cy="7" r="7" fill="#e5662a"/>
          <path d="M4.5 3.5 L6 3.5 L6.6 5.3 L5.7 6 Q6.5 7.7 8 8.3 L8.7 7.4 L10.5 8 L10.5 9.5 Q7 10 4.5 5.5 Z" fill="#050507"/>
        </svg>
        <span>: 013 05518842</span>
      </li>
      <li class="contact__item">
        <svg class="contact__icon" width="14" height="14" viewBox="0 0 14 14" aria-hidden="true">
          <circle cx="7" cy="7" r="7" fill="#e5662a"/>
          <rect x="3.5" y="4.5" width="7" height="5" fill="none" stroke="#050507" stroke-width="1.2"/>
          <path d="M3.5 4.5 L7 7.5 L10.5 4.5" fill="none" stroke="#050507" stroke-width="1.2"/>
        </svg>
        <span>: info@velbiro.com</span>
      </li>
      <li class="contact__item contact__item--address">
        <svg class="contact__icon" width="14" height="14" viewBox="0 0 14 14" aria-hidden="true">
          <circle cx="7" cy="7" r="7" fill="#e5662a"/>
          <path d="M7 3 A2.6 2.6 0 0 1 9.6 5.6 Q9.6 7.5 7 11 Q4.4 7.5 4.4 5.6 A2.6 2.6 0 0 1 7 3 Z" fill="#050507"/>
          <circle cx="7" cy="5.6" r="1" fill="#e5662a"/>
        </svg>
        <address style="font-style:normal">: 27 Marlow Street<br>#09-04 Westbrook Tower<br>Singapore 048216</address>
      </li>
    </ul>

    <p class="website">WWW.VELBIRO.COM</p>
  </section>

</main>
</body>
</html>
```